Food menu for Maplewood Rally LLC

We need a menu that is visually captivating but not difficult to read. Maplewood Rally is an activity based bar located in Chattanooga TN. We have 10 bowling lanes, corn hole, ping pong, shuffleboard, billiards, darts, skee ball machines, pin ball, ring toss, and giant jenga. We have a huge venue that seats over 350 guests and is one of the largest in Chattanooga TN. Our original menu creation was professionally done but due to management conflicts we lost the ability to continue using it. Since then, we've been stuck printing menus on word and it's embarrassing.

Our initial product is selling good quality food on a large scale. Our secondary product is offering free games to all patrons (except for bowling). The original menu had a fold out piece, but I'm not married to that. Also - though cute - we no longer have the best BBQ in town (voted by me) so it no longer needs to be a thing. I don't want a recreation of our original menu - I just love it very much and find it creative.

Our colors are a light navy blue, light yellow, red, and black. We have custom built interior using giant black metal beams and custom black handrails. Hardwood floors and beautiful polished concrete floors. The Quiet Harbinger plays a huge role in the theme.

The final design should be relevant to our logo : "Feast. Sip. Roll." The prices and food item descriptions on the "MENU LEGAL DESIGN CROWD" file are all correct. The brandbook has our logo's and other misc. icons. We don't have a swimming pool so wouldn't use that one. The Check Presenter file is the current iteration of the Logo format.

Target Market(s)

Men and Women between the ages of 25-45

Industry/Entity Type

Restaurant

Font styles to use
Sans Serif
Other font styles liked:
• Mench

Colors

Designer to choose colors to be used in the design.

Requirements
Must have
• Easy to read descriptions
• Information about all the games available to guests
• All the information present in the word document menu
Nice to have
• White space (not a fan of cramming it all in)
• Double sided or fold over menu. Not married to anything yet. Curious to see what people come up with.
• Visuals about bowling (the OG lanes on the side panel, etc)

```html
<!DOCTYPE html>
<html lang="en">
<head>
<meta charset="utf-8">
<title>Maplewood Rally Menu</title>
<link rel="stylesheet" href="https://fonts.googleapis.com/css2?family=Bebas+Neue&family=Archivo+Narrow:wght@400;600;700&family=Oswald:wght@300;400&display=swap">
<style>
:root{
  --gold:#b07f3c;
  --ink:#222;
  --soft:#555;
  --paper:#fff;
  --stage:#e9e6e1;
  --cover-yellow:#efe98f;
}
*{box-sizing:border-box;margin:0;padding:0}
html,body{width:1200px;height:1200px;overflow:hidden;background:var(--stage)}
body{position:relative;font-family:"Archivo Narrow",sans-serif;color:var(--ink)}
.page{position:absolute;width:413px;height:530px;background:var(--paper);overflow:hidden}
.frame{position:absolute;inset:18px 16px;border:1.5px solid var(--gold);border-radius:18px;pointer-events:none}
.cover{left:193px;top:49px;background:radial-gradient(ellipse at 25% 10%,var(--cover-yellow) 0%,#f5f2c4 45%,#fdfdf6 100%)}
.cover .frame{border-color:#c9a46a}
.inside-a{left:606px;top:49px}
.inside-b{left:195px;top:620px}
.inside-c{left:608px;top:620px}

.brand-name{position:absolute;left:80px;top:100px;font-family:"Bebas Neue",sans-serif;font-size:46px;line-height:.9;color:var(--ink);letter-spacing:1px}
.hero-photo{position:absolute;left:130px;top:165px;width:283px;height:255px;border-radius:50% 0 0 50%;background:radial-gradient(circle at 55% 50%,#c9763a 0%,#d89a54 45%,#b37a48 70%,rgba(255,255,255,0) 72%)}
.tagline{position:absolute;left:0;right:0;top:448px;text-align:center}
.tag-icons{display:flex;justify-content:center;gap:14px;align-items:center}
.tag-icons .sep{width:1px;height:24px;background:var(--ink)}
.tag-words{margin-top:8px;font-family:"Oswald",sans-serif;font-weight:300;font-size:14px;letter-spacing:2px;display:flex;justify-content:center;gap:16px}

.watermark{position:absolute;right:40px;top:34px;font-family:"Bebas Neue",sans-serif;font-size:16px;color:var(--gold);opacity:.25;letter-spacing:1px}
.col{position:absolute}
.section-title{font-family:"Bebas Neue",sans-serif;font-size:24px;color:var(--gold);letter-spacing:.5px;line-height:1;margin-bottom:4px}
.section-title small{font-family:"Archivo Narrow",sans-serif;font-size:8px;color:var(--ink);letter-spacing:0;margin-left:4px}
.section-note{font-size:7px;margin:-2px 0 4px}
.item{margin-bottom:8px}
.item-row{display:flex;align-items:baseline;font-weight:700;font-size:8.5px}
.item-row .leader{flex:1;border-bottom:1px dotted var(--ink);margin:0 2px;transform:translateY(-2px)}
.desc{font-size:6.2px;line-height:1.3;color:var(--soft);margin-top:1px}
.desc b{color:var(--ink)}
.rule{border-top:1.2px solid var(--ink);margin:8px 0 10px}
.vrule{position:absolute;width:1px;background:var(--ink)}
.legal{position:absolute;left:58px;right:32px;bottom:28px;font-size:5.2px;line-height:1.35;color:var(--soft);border-top:1px solid var(--ink);padding-top:5px}
.foot-icon{position:absolute;left:30px;bottom:26px}

.games{position:absolute;left:60px;top:30px;display:flex;gap:6px}
.games .free{writing-mode:vertical-rl;transform:rotate(180deg);font-family:"Bebas Neue",sans-serif;font-size:14px;color:var(--gold);letter-spacing:1px}
.games h3{font-family:"Archivo Narrow",sans-serif;font-weight:600;font-size:9px;color:var(--gold)}
.games p{font-family:"Oswald",sans-serif;font-weight:300;font-size:8.5px;letter-spacing:.6px;line-height:1.6}
.plain-list{font-weight:700;font-size:8.5px;line-height:1.25}
.gf{font-size:6px;text-align:center;margin:8px 0 10px;font-weight:600}
</style>
</head>
<body>

<section class="page cover">
  <div class="frame"></div>
  <div class="brand-name">MAPLEWOOD<br>RALLY</div>
  <div class="hero-photo" role="img" aria-label="Photo of a sliced supreme pizza on a wooden board with bowling pins behind it"></div>
  <div class="tagline">
    <div class="tag-icons">
      <svg width="22" height="22" viewBox="0 0 22 22" fill="none" stroke="#222" stroke-width="1.5"><path d="M3 3l16 16M19 3L3 19"/></svg>
      <span class="sep"></span>
      <svg width="22" height="22" viewBox="0 0 22 22" fill="none" stroke="#222" stroke-width="1.5"><path d="M3 4h16l-8 8zM11 12v7M7 19h8"/></svg>
      <span class="sep"></span>
      <svg width="22" height="22" viewBox="0 0 22 22" fill="none" stroke="#222" stroke-width="1.5"><circle cx="11" cy="11" r="8"/><circle cx="9" cy="8" r="1"/><circle cx="12" cy="7" r="1"/><circle cx="11" cy="10" r="1"/></svg>
    </div>
    <div class="tag-words"><span>FEAST.</span><span>SIP.</span><span>ROLL.</span></div>
  </div>
</section>

<section class="page inside-a">
  <div class="frame"></div>
  <div class="watermark">MAPLEWOOD RALLY</div>
  <div class="col" style="left:30px;top:86px;width:168px">
    <h2 class="section-title">APPETIZERS</h2>
    <div class="item"><div class="item-row">Maplewood Sampler<span class="leader"></span>$13</div><div class="desc"><b>Your choice of 3:</b> Smoked Wings, Boneless Wings, Mac Bites, Fried Pickles, Fried Green Tomatoes, Mango Habanero Shrimp, Pretzel, Mozzarella Sticks.<br>Served with Carrots, Celery, and dipping sauces</div></div>
    <div class="item"><div class="item-row">Fried Pickle Spears<span class="leader"></span>$8</div><div class="desc">Mesquite battered, served with a side of Chipotle Ranch</div></div>
    <div class="item"><div class="item-row">Fried Green Tomatoes<span class="leader"></span>$8</div><div class="desc">Served on a bed of Southern Slaw, topped with Cajun Remoulade</div></div>
    <div class="item"><div class="item-row">Pepper Jack &amp; Mac &amp; Cheese Bites<span class="leader"></span>$9</div><div class="desc">House-made and fried, served on a bed of Marinara</div></div>
    <div class="item"><div class="item-row">Mango Habanero Shrimp<span class="leader"></span>$9</div><div class="desc">Panko fried, tossed in a Sweet and Spicy Sauce on a bed of Southern Slaw</div></div>
    <div class="item"><div class="item-row">Meatballs<span class="leader"></span>$9</div><div class="desc">House-made, served on a bed of Marinara</div></div>
    <div class="item"><div class="item-row">Mozzarella Sticks<span class="leader"></span>$8</div><div class="desc">Fried, served with a side of Marinara</div></div>
    <div class="item"><div class="item-row">Nachos<span class="leader"></span>$8</div><div class="desc">Chili, Cheese, Pico de Gallo, and Sour Cream. Add <b>Chicken or Beef – 1</b></div></div>
    <div class="item"><div class="item-row">Tot-chos<span class="leader"></span>$9</div><div class="desc">Chili, Cheese, Pico de Gallo, Avocado, and Sour Cream</div></div>
    <div class="item"><div class="item-row">Pretzels<span class="leader"></span>$9</div><div class="desc">Served with a side of Beer Cheese</div></div>
    <div class="item"><div class="item-row">Truffle Fries<span class="leader"></span>$9</div><div class="desc">Truffle Oil, Garlic, Parmesan Cheese, and Parsley</div></div>
  </div>
  <div class="vrule" style="left:206px;top:80px;height:390px"></div>
  <div class="col" style="left:215px;top:82px;width:165px">
    <div class="item"><div class="item-row">Loaded Fries<span class="leader"></span>$8</div><div class="desc">Bacon, Cheddar, and Sour Cream</div></div>
    <div class="item"><div class="item-row">Roasted Red Pepper Hummus<span class="leader"></span>$9</div><div class="desc">Pita Wedges, Carrots, and Celery</div></div>
    <div class="item"><div class="item-row">Chips and Dip<span class="leader"></span>$8</div><div class="desc">Pita Wedges or Tortilla Chips Served with your choice of: Buffalo Chicken, Queso, or Spinach Dip<br><b>Get All Three Dips for 10</b></div></div>
    <div class="item"><div class="item-row">Chips and Salsa<span class="leader"></span>$5</div><div class="desc">Tortilla Chips served with our House-made Salsa</div></div>
    <div class="rule"></div>
    <h2 class="section-title">SANDWICHES</h2>
    <p class="section-note">(Served with one side)</p>
    <div class="item"><div class="item-row">Chicken Bacon Ranch Sandwich<span class="leader"></span>$12</div><div class="desc">Grilled Chicken Breast, Bacon, Pepper Jack, Avocado, Ranch, Lettuce, and Tomato on a Brioche Bun</div></div>
    <div class="item"><div class="item-row">Buffalo Chicken Sandwich<span class="leader"></span>$12</div><div class="desc">Buffalo Tossed Fried Chicken Breast, Lettuce, and Tomato on a Brioche Bun</div></div>
    <div class="item"><div class="item-row">Maple-Cuban<span class="leader"></span>$11</div><div class="desc">Pulled Pork, Ham, Swiss, Pickles, and Grain Mustard on Cuban Bread</div></div>
    <div class="item"><div class="item-row">Rally Cheese Steak<span class="leader"></span>$10</div><div class="desc">Shaved Steak, Swiss, Roasted Red &amp; Green Peppers, and Sautéed Onion on French Bread</div></div>
    <div class="item"><div class="item-row">French Dip<span class="leader"></span>$11</div><div class="desc">Smoked Brisket and Swiss on French Bread Served with a side of Au Jus</div></div>
    <div class="item"><div class="item-row">Pulled Pork Sandwich<span class="leader"></span>$10</div><div class="desc">Pulled Pork, Southern Slaw, and BBQ Sauce on a Brioche Bun</div></div>
  </div>
  <svg class="foot-icon" width="24" height="24" viewBox="0 0 24 24" fill="none" stroke="#bbb" stroke-width="2"><path d="M3 3l18 18M21 3L3 21"/></svg>
  <p class="legal">Parties of eight or more people are subject to a 20% service charge. *Consuming raw or undercooked meats, poultry, seafood, shellfish, or eggs may increase your risk of foodborne illness*</p>
</section>

<section class="page inside-b">
  <div class="frame"></div>
  <div class="watermark">MAPLEWOOD RALLY</div>
  <div class="games">
    <span class="free">FREE</span>
    <div>
      <h3>GAMES LOCATED IN OUR BOWLING CAGE</h3>
      <p>• BILLIARDS • FOOSBALL • CORNHOLE<br>• PING PONG • DARTS • SHUFFLEBOARD</p>
    </div>
  </div>
  <div class="col" style="left:32px;top:84px;width:165px">
    <div class="item"><div class="item-row">Maplewood Burger<span class="leader"></span>$11</div><div class="desc">Beef Patty, Cheese, Lettuce, Tomato, and Onion on a Brioche Bun</div></div>
    <div class="item"><div class="item-row">Patty Melt<span class="leader"></span>$11</div><div class="desc">Two Beef Patties, Bacon, Cheese, Sautéed Onion, and Steak Sauce Aioli on Texas Toast</div></div>
    <div class="item"><div class="item-row">BBQ Bacon Cheeseburger<span class="leader"></span>$12</div><div class="desc">Beef Patty, Bacon, Cheese, BBQ Sauce, Lettuce, Tomato, and Onion on a Brioche Bun</div></div>
    <div class="item"><div class="item-row">Pimento Cheeseburger<span class="leader"></span>$12</div><div class="desc">Beef Patty, Pimento Cheese, Lettuce, Tomato, and Onion on a Brioche Bun</div></div>
    <div class="item"><div class="item-row">Bison Burger<span class="leader"></span>$14</div><div class="desc">Bison Patty (best cooked medium), Smoked Gouda, BBQ Sauce, Lettuce, Tomato, and Onion on a Brioche Bun</div></div>
    <div class="item"><div class="item-row">Turkey Burger<span class="leader"></span>$11</div><div class="desc">Ground Turkey Patty, Steak Sauce Aioli, Lettuce, Tomato, and Onion on a Brioche Bun<br><b>Cheese –</b> Cheddar, Mozzarella, Pepper Jack, Pimento, Smoked Gouda, Swiss</div></div>
    <p class="gf">*Gluten-Free Buns available upon request*</p>
    <div class="rule" style="margin-top:0"></div>
    <h2 class="section-title">ENTRÉES</h2>
    <div class="item"><div class="item-row">Smoked Baby Back Ribs<span class="leader"></span>$13</div><div class="desc">Full Slab, Garlic Dinner Roll, and your choice of two sides</div></div>
    <div class="item"><div class="item-row">Shaved Smoked Brisket<span class="leader"></span>$13</div><div class="desc">Au Jus, Garlic Dinner Roll, and your choice of two sides</div></div>
    <div class="item"><div class="item-row">Pulled Pork Platter<span class="leader"></span>$12</div><div class="desc">Smoked, Garlic Dinner Roll, and your choice of two sides</div></div>
  </div>
  <div class="vrule" style="left:206px;top:86px;height:340px"></div>
  <div class="col" style="left:213px;top:84px;width:166px">
    <div class="item"><div class="item-row">Grilled Salmon<span class="leader"></span>$13</div><div class="desc">Bourbon Glaze, Garlic Dinner Roll, and your choice of two sides</div></div>
    <div class="item"><div class="item-row">Shrimp &amp; Grits<span class="leader"></span>$12</div><div class="desc">Jumbo Shrimp, Fried Green Tomatoes, Black-Eyed Peas, Red &amp; Green Peppers, Cajun Butter</div></div>
    <div class="item"><div class="item-row">Wings<span class="leader"></span>$11</div><div class="desc">Traditional or Boneless, tossed in your choice of: Mild, Hot, Extra Hot, BBQ, Bourbon Glaze, Lemon Pepper, Garlic Parmesan, or Mango Habanero. Served with Celery, Carrots, and Ranch or Bleu Cheese</div></div>
    <div class="item"><div class="item-row">Chicken Fingers<span class="leader"></span>$11</div><div class="desc">Blackened, Grilled, or Fried, served with one side and dipping sauce. Choose from: BBQ, Honey Mustard, Bleu Cheese, or Ranch</div></div>
    <div class="item"><div class="item-row">Fish and Chips<span class="leader"></span>$11</div><div class="desc">Atlantic Cod, Southern Slaw, Tartar Sauce, and Fries</div></div>
    <div class="item"><div class="item-row">Quesadilla<span class="leader"></span>$11</div><div class="desc">Chicken or Steak, Roasted Red &amp; Green Peppers, Sautéed Onions, and Mixed Cheese</div></div>
    <div class="item"><div class="item-row">Veggie Bowl<span class="leader"></span>$9</div><div class="desc">Kale, Red &amp; Green Peppers, Onions, Zucchini, Yellow Squash, and Fried Green Tomatoes over a bed of Grits or Mashed Potatoes<br>Add Chicken – 3 &nbsp; Add Salmon or Shrimp – 4</div></div>
    <div class="rule"></div>
    <h2 class="section-title">SALADS</h2>
    <div class="item"><div class="item-row">House Salad<span class="leader"></span>$7</div><div class="desc">Mixed Greens, Carrots, Cucumber, Tomato</div></div>
    <div class="item"><div class="item-row">Caesar Salad<span class="leader"></span>$7</div><div class="desc">Romaine, Parmesan, Croutons, Caesar Dressing</div></div>
  </div>
  <svg class="foot-icon" width="24" height="24" viewBox="0 0 24 24" fill="none" stroke="#bbb" stroke-width="1.5"><path d="M3 4h18l-9 9zM12 13v8M8 21h8"/></svg>
  <p class="legal">Parties of eight or more people are subject to a 20% service charge. *Consuming raw or undercooked meats, poultry, seafood, shellfish, or eggs may increase your risk of foodborne illness*</p>
</section>

<section class="page inside-c">
  <div class="frame"></div>
  <div class="watermark">MAPLEWOOD RALLY</div>
  <div class="col" style="left:30px;top:84px;width:168px">
    <div class="item"><div class="item-row">Southwestern Salad<span class="leader"></span>$7</div><div class="desc">Mixed Greens, Black Beans, Corn, Tortilla Chips, Santa Fe Dressing</div></div>
    <div class="item"><div class="item-row">Harvest Salad<span class="leader"></span>$9</div><div class="desc">Mixed Greens, Carrots, Feta, Onions, Tomatoes, Mandarin Oranges, Shaved Almonds</div></div>
    <div class="item"><div class="item-row">Cobb Salad<span class="leader"></span>$9</div><div class="desc">Mixed Greens, Eggs, Bleu Cheese, Bacon, Avocado, Tomatoes<br>Add Chicken – $3 &nbsp; Add Salmon or Shrimp – $4<br><b>Dressings –</b> Balsamic Vinaigrette, Blood Orange Vinaigrette, Bleu Cheese, Honey Mustard, Santa Fe, Ranch, Chipotle Ranch</div></div>
    <div class="rule"></div>
    <h2 class="section-title">TACOS <small>(3 per order)</small></h2>
    <p class="desc" style="margin-bottom:6px">All Tacos served with a side of Sour Cream and Lime Wedge</p>
    <div class="item"><div class="item-row">Chicken<span class="leader"></span>$9</div><div class="desc">Shredded Chicken, Mozzarella, Avocado, Pico de Gallo, and Lettuce</div></div>
    <div class="item"><div class="item-row">Beef<span class="leader"></span>$9</div><div class="desc">Beef, Mozzarella, Avocado, Pico de Gallo, and Lettuce</div></div>
    <div class="item"><div class="item-row">Pork<span class="leader"></span>$9</div><div class="desc">Smoked Pork, Mozzarella, Avocado, Pico de Gallo, and Lettuce</div></div>
    <div class="item"><div class="item-row">Fish<span class="leader"></span>$9</div><div class="desc">Fried Cod, Pico de Gallo, Lettuce, and Cajun Remoulade</div></div>
    <div class="item"><div class="item-row">Shrimp<span class="leader"></span>$10</div><div class="desc">Blackened Shrimp, Mango Salsa, and Lettuce</div></div>
  </div>
  <div class="vrule" style="left:206px;top:86px;height:380px"></div>
  <div class="col" style="left:214px;top:80px;width:165px">
    <h2 class="section-title">PIZZAS <small>(14 inch)</small></h2>
    <div class="item" style="margin-bottom:4px"><div class="item-row">Cheese Pizza<span class="leader"></span>$10</div><div class="item-row">Toppings<span class="leader"></span>$1</div><div class="desc"><b>Meats –</b> Bacon, Beef, Chicken, Ham, Meatballs, Pepperoni, Pork, Sausage<br><b>Cheeses –</b> Cheddar, Parmesan, Pepper Jack, Mozzarella<br><b>Veggies –</b> Artichokes, Banana Peppers, Black Olives, Green Peppers, Jalapeños, Mushrooms, Onions, Pineapples, Roasted Red Peppers, and Sundried Tomatoes</div></div>
    <div class="item"><div class="item-row">Margherita Pizza<span class="leader"></span>$13</div><div class="desc">Fresh Mozzarella, Sundried Tomatoes, and Basil</div></div>
    <div class="rule"></div>
    <h2 class="section-title">SIDES</h2>
    <div class="item"><div class="plain-list">Baked Beans, Broccoli, Chili, French Fries, Mashed Potatoes, Mixed Fruit, Mixed Veggies, Onion Rings, Pepper Jack Mac &amp; Cheese, Southern Slaw,</div><div class="item-row">Tater Tots<span class="leader" style="border:0"></span>$3</div></div>
    <div class="item"><div class="plain-list">Side House Salad, Side Caesar,</div><div class="item-row">Sweet Potato Waffle Fries<span class="leader"></span>$4</div></div>
    <div class="item"><div class="item-row">Truffle Fries<span class="leader"></span>$5</div></div>
    <div class="rule"></div>
    <h2 class="section-title">SOFT DRINKS</h2>
    <div class="plain-list">Cola, Diet Cola, Lemon-Lime, Pepper Soda, Root Beer, Lemonade, Sweet Tea, Unsweet Tea</div>
    <div class="item-row" style="justify-content:flex-end">$2.50</div>
  </div>
  <svg class="foot-icon" width="24" height="24" viewBox="0 0 24 24" fill="none" stroke="#bbb" stroke-width="1.5"><circle cx="12" cy="12" r="9"/><circle cx="10" cy="8" r="1"/><circle cx="13" cy="7.5" r="1"/><circle cx="12" cy="11" r="1"/></svg>
  <p class="legal">Parties of eight or more people are subject to a 20% service charge. *Consuming raw or undercooked meats, poultry, seafood, shellfish, or eggs may increase your risk of foodborne illness*</p>
</section>

</body>
</html>
```